IT services company requires Letterhead design

We need a professional letterhead designed to be used for general correspondence with customers, quotes, invoices etc. We are a new IT services company specialising in computer servicing and repairs and mobile and tablet repairs. Attached are templates that my printing company have supplied, my logos, an interpretation of our website for you to get a feel of the company. Details to be included on the letterhead are

Company Number – 4738261
VAT Number - 518337942
Registered Address – 14-16 Brambly Lane, London, E4 9QT

Phone – 01632 487215
Email – sales@quorvent.com
Web – www.quorvent.com

I would prefer for the top of the letterhead to just have the company logo on a white background and the rest of the details on the bottom of the letterhead but I am open to design ideas.

Thanks

```html
<!DOCTYPE html>
<html lang="en">
<head>
<meta charset="utf-8">
<title>Quorvent Letterhead</title>
<link href="https://fonts.googleapis.com/css2?family=Questrial&display=swap" rel="stylesheet">
<style>
  :root {
    --brand-blue: #0b7cc4;
    --text-blue: #1a72c0;
    --ink: #2b2b2b;
    --rule: #3a9bc9;
    --paper: #ffffff;
    --edge: #cfcfcf;
  }
  * { margin: 0; padding: 0; box-sizing: border-box; }
  html, body { width: 853px; height: 1200px; overflow: hidden; background: var(--paper); }
  body { font-family: "Questrial", "Century Gothic", sans-serif; }
  .letterhead {
    position: relative;
    width: 853px;
    height: 1200px;
    background: var(--paper);
    border: 1px solid var(--edge);
    overflow: hidden;
  }
  .header-band { position: absolute; top: 0; left: 0; width: 853px; height: 154px; }
  .brand-pill {
    position: absolute;
    top: 20px;
    left: 352px;
    width: 520px;
    height: 108px;
    background: var(--paper);
    border-radius: 54px 0 0 54px;
  }
  .brand-mark {
    position: absolute;
    top: 62px;
    left: 400px;
    display: flex;
    align-items: center;
    gap: 12px;
  }
  .brand-square { width: 16px; height: 16px; background: var(--brand-blue); }
  .brand-name { font-size: 36px; color: var(--brand-blue); line-height: 1; }
  .sender {
    position: absolute;
    top: 20px;
    right: 14px;
    text-align: right;
    white-space: nowrap;
  }
  .sender-name { font-size: 34px; color: var(--ink); line-height: 1.05; }
  .sender-role { font-size: 19px; color: var(--text-blue); margin-top: 4px; }
  .sender-phone { font-size: 19px; color: var(--text-blue); margin-top: 14px; }
  .footer-rule {
    position: absolute;
    top: 1105px;
    left: 17px;
    width: 832px;
    height: 1px;
    background: var(--rule);
  }
  .footer-details {
    position: absolute;
    top: 1117px;
    font-size: 18px;
    line-height: 23px;
    color: var(--text-blue);
    white-space: nowrap;
  }
  .company-details { left: 22px; }
  .contact-details { right: 20px; }
</style>
</head>
<body>
  <div class="letterhead">
    <svg class="header-band" viewBox="0 0 853 154" aria-hidden="true">
      <path fill="var(--brand-blue)" d="M0 0 H205 C215 0 225 14 242 14 C259 14 269 0 279 0 H853 V154 H300 C268 154 270 104 238 104 C206 104 208 154 176 154 H0 Z"/>
    </svg>
    <div class="brand-pill"></div>
    <div class="brand-mark">
      <span class="brand-square"></span>
      <span class="brand-name">Quorvent</span>
    </div>
    <div class="sender">
      <div class="sender-name">Daniel Hartley</div>
      <div class="sender-role">Director</div>
      <div class="sender-phone">01632 487215</div>
    </div>

    <div class="footer-rule"></div>
    <div class="footer-details company-details">
      <p>Company Number - 4738261</p>
      <p>VAT Number - 518337942</p>
      <p>Registered Address - 14-16 Brambly Lane, London, E4 9QT</p>
    </div>
    <div class="footer-details contact-details">
      <p>Phone - 01632 487215</p>
      <p>Email - sales@quorvent.com</p>
      <p>Web - www.quorvent.com</p>
    </div>
  </div>
</body>
</html>
```